Logo redesign & Stationery Design Project

We need a logo redesign for our company.

We also require the following stationary with the new logo:
*letterhead
*With compliments slips
*business card
*envelopes

We would like to maintain our current colours of navy blue and gold. We would like to maintain the wording on the back of our current business card.

Our existing letterhead and business card is attached.

Target Market(s)

Medical Professionals, Pharmacists, Lawyers

Industry/Entity Type

Business

Requirements
Must have
• See attached business card and letterhead, as all details on these documents need to be included.

```html
<!DOCTYPE html>
<html lang="en">
<head>
<meta charset="utf-8">
<title>Halden Marsh Financial Services – Business Card</title>
<link rel="stylesheet" href="https://fonts.googleapis.com/css2?family=Bebas+Neue&family=Questrial&display=swap">
<style>
  :root {
    --navy: #25206b;
    --gold: #d49a2a;
    --card: #e8e8e8;
    --ink: #2a2a2a;
    --backdrop: #3b3b3b;
    --tint: rgba(212, 154, 42, 0.18);
  }
  * { margin: 0; padding: 0; box-sizing: border-box; }
  html, body { width: 1200px; height: 900px; overflow: hidden; }
  body {
    background: var(--backdrop);
    position: relative;
    font-family: "Questrial", "Century Gothic", sans-serif;
    color: var(--ink);
  }
  .card {
    position: absolute;
    top: 300px;
    width: 525px;
    height: 300px;
    background: var(--card);
    border-radius: 22px;
    overflow: hidden;
  }
  .card--front { left: 58px; }
  .card--back { left: 617px; }

  .wordmark {
    font-family: "Bebas Neue", sans-serif;
    color: var(--navy);
    font-weight: 400;
    line-height: 0.95;
  }
  .front-brand {
    position: absolute;
    left: 42px;
    top: 46px;
    display: flex;
    align-items: center;
    gap: 12px;
  }
  .brand-dot {
    width: 64px; height: 64px;
    border-radius: 50%;
    background: var(--gold);
    flex: none;
  }
  .front-brand .wordmark { font-size: 30px; }

  .faint-circle {
    position: absolute;
    left: 350px;
    top: 5px;
    width: 300px;
    height: 300px;
    border-radius: 50%;
    background: var(--tint);
  }

  .contact {
    position: absolute;
    left: 55px;
    top: 157px;
    font-size: 14px;
    line-height: 1.2;
  }
  .contact__name { color: var(--navy); font-weight: 700; font-size: 16px; }
  .contact__role { font-size: 14px; margin-bottom: 13px; }
  .contact__address { margin-bottom: 12px; }
  .contact__label { color: var(--gold); }
  .contact__web { color: var(--gold); font-size: 17px; }

  .back-brand {
    position: absolute;
    left: 0; right: 0;
    top: 57px;
    display: flex;
    flex-direction: column;
    align-items: center;
    padding-left: 142px;
  }
  .back-brand .brand-dot { width: 114px; height: 114px; margin-bottom: 16px; }
  .back-brand .wordmark { font-size: 50px; text-align: center; }
  .back-brand .wordmark span { display: block; font-size: 24px; letter-spacing: 3px; }
</style>
</head>
<body>
  <section class="card card--front">
    <div class="faint-circle" aria-hidden="true"></div>
    <div class="front-brand">
      <div class="brand-dot" aria-hidden="true"></div>
      <div class="wordmark">Halden Marsh</div>
    </div>
    <div class="contact">
      <p class="contact__name">Daniel (Dan) Halden</p>
      <p class="contact__role">Partner</p>
      <p class="contact__address">Suite 4, 118 Harbour Road, Bayview</p>
      <p><span class="contact__label">t :</span> 02 9100 4271 <span class="contact__label">m :</span> 0400 318 562</p>
      <p><span class="contact__label">e :</span> dan@haldenmarsh.com.au</p>
      <p class="contact__web">www.haldenmarsh.com.au</p>
    </div>
  </section>

  <section class="card card--back">
    <div class="back-brand" style="padding-left:140px">
      <div class="brand-dot" aria-hidden="true"></div>
      <div class="wordmark">Halden Marsh<span>Financial Services</span></div>
    </div>
  </section>
</body>
</html>
```